Kestrelguard Letterhead and Template Design

We are looking to freshen up and modernise our business letter heads and cover pages for our documents. Looking at a suit of new designs. I would like a design for:
- Letter Head
- Page 2 follower (for lengthy documents) - fancy
- Page 2 follower (for lengthy documents) - simple version
- Cover Page for reports to sent to client
- Cover Page for internal documents.

Our website is www.kestrelguard-example.com.au.

I have attached a copy of our current brochure for inspiration and our old letter head so you can see what we currently use.

On our Client Cover Page and letter head we would like to include out business awards. Happy for you to change these designs if you have something that would look better. Have also included logos and awards. We won the Coastal Vermin Controller Prize in 2022/23 and also in 2019/2020. We were a state finalist in the Orvane Enterprise Honours this year logo attached.

We like the emblem to be watermarked into the page in the background.

We want something fresh/clean/modern and classy.

Letter head needs to include our Phone Number: 1300555019
Email: hello@kestrelguard-example.com.au
Text: 0400555382
Website: www.kestrelguard-example.com.au

```html
<!DOCTYPE html>
<html lang="en">
<head>
<meta charset="utf-8">
<title>Kestrelguard Letterhead</title>
<link href="https://fonts.googleapis.com/css2?family=Lato:wght@400;700&display=swap" rel="stylesheet">
<style>
  :root {
    --backdrop: #dcdcdc;
    --paper: #ffffff;
    --brand-green: #7bc043;
    --charcoal: #474545;
    --watermark: #ededed;
    --gold-light: #efdca0;
    --gold-mid: #d3b569;
    --gold-dark: #b8954a;
    --footer-text: #ffffff;
  }
  * { margin: 0; padding: 0; box-sizing: border-box; }
  html, body {
    width: 1200px;
    height: 947px;
    overflow: hidden;
    background: var(--backdrop);
    font-family: "Lato", sans-serif;
  }
  .letterhead {
    position: absolute;
    left: 364px;
    top: 179px;
    width: 472px;
    height: 605px;
    background: var(--paper);
    overflow: hidden;
  }
  .page-art {
    position: absolute;
    inset: 0;
    width: 472px;
    height: 605px;
  }
  .brand {
    position: absolute;
    left: 276px;
    top: 16px;
    display: flex;
    align-items: center;
    gap: 7px;
  }
  .brand-dot {
    width: 24px;
    height: 24px;
    border-radius: 50%;
    background: var(--brand-green);
  }
  .brand-name {
    font-weight: 700;
    font-size: 21px;
    letter-spacing: 0.2px;
    color: var(--charcoal);
  }
  .contact {
    position: absolute;
    top: 575px;
    display: flex;
    flex-direction: column;
    gap: 1px;
    font-size: 9px;
    line-height: 10px;
    color: var(--footer-text);
  }
  .contact-phone { left: 44px; }
  .contact-web { left: 137px; }
  .contact-line {
    display: flex;
    align-items: center;
    gap: 4px;
    white-space: nowrap;
  }
  .contact-icon { width: 8px; height: 8px; flex: none; }
</style>
</head>
<body>
  <main class="letterhead">
    <svg class="page-art" viewBox="0 0 472 605" aria-hidden="true">
      <defs>
        <linearGradient id="gold-ribbon" x1="0" y1="1" x2="1" y2="0">
          <stop offset="0" stop-color="var(--gold-dark)"/>
          <stop offset="0.35" stop-color="var(--gold-light)"/>
          <stop offset="0.7" stop-color="var(--gold-mid)"/>
          <stop offset="1" stop-color="var(--gold-light)"/>
        </linearGradient>
      </defs>
      <polygon class="corner-accent" points="0,0 90,0 0,52" fill="var(--brand-green)"/>
      <circle class="watermark-mark" cx="236" cy="302" r="95" fill="var(--watermark)"/>
      <polygon class="footer-band" points="0,568 368,568 331,605 0,605" fill="var(--charcoal)"/>
      <polygon class="award-ribbon" points="331,605 386,605 472,519 472,464" fill="url(#gold-ribbon)"/>
      <g class="award-seal">
        <circle cx="440" cy="527" r="29" fill="var(--gold-mid)"/>
        <circle cx="440" cy="527" r="24" fill="var(--paper)"/>
      </g>
      <g class="award-seal">
        <circle cx="393" cy="573" r="29" fill="var(--gold-mid)"/>
        <circle cx="393" cy="573" r="24" fill="var(--paper)"/>
      </g>
    </svg>

    <header class="brand">
      <span class="brand-dot"></span>
      <span class="brand-name">Kestrelguard</span>
    </header>

    <footer>
      <div class="contact contact-phone">
        <div class="contact-line">
          <svg class="contact-icon" viewBox="0 0 10 10"><path d="M2 1 L4 1 L4.6 3 L3.4 3.8 Q4.4 5.8 6.2 6.6 L7 5.4 L9 6 L9 8 Q9 9 8 9 Q1 8.4 1 2 Q1 1 2 1Z" fill="var(--brand-green)"/></svg>
          <span>1300555019</span>
        </div>
        <div class="contact-line">
          <svg class="contact-icon" viewBox="0 0 10 10"><rect x="2.5" y="0.5" width="5" height="3" fill="var(--brand-green)"/><rect x="0.5" y="3.5" width="9" height="4" rx="1" fill="var(--brand-green)"/><rect x="2.5" y="6.5" width="5" height="3" fill="var(--brand-green)"/></svg>
          <span>0400555382</span>
        </div>
      </div>
      <div class="contact contact-web">
        <div class="contact-line">
          <svg class="contact-icon" viewBox="0 0 10 10"><rect x="0.5" y="2" width="9" height="6.5" fill="var(--brand-green)"/><path d="M0.5 2 L5 5.6 L9.5 2" stroke="var(--charcoal)" stroke-width="0.8" fill="none"/></svg>
          <span>hello@kestrelguard-example.com.au</span>
        </div>
        <div class="contact-line">
          <svg class="contact-icon" viewBox="0 0 10 10"><circle cx="5" cy="5" r="4.3" fill="none" stroke="var(--brand-green)" stroke-width="1"/><ellipse cx="5" cy="5" rx="1.8" ry="4.3" fill="none" stroke="var(--brand-green)" stroke-width="0.8"/><path d="M0.7 5 H9.3" stroke="var(--brand-green)" stroke-width="0.8"/></svg>
          <span>www.kestrelguard-example.com.au</span>
        </div>
      </div>
    </footer>
  </main>
</body>
</html>
```